Non-Profit Organization Needs WordPress websiteTo Empower Women

Our client is a Non-profit organization that requires a responsively-designed WordPress website to help publish their online magazine. This website will also feature their magazine publication that they publish quarterly. The design will need to be mobile-friendly, so it looks great on all devices.

The main purpose of this site is the following, in order of importance:
1. Educate economically-challenged women to improve their lives with blog content and their online Magazine.
2. Create a Membership community for these women to help one another. THE MAIN CALL-TO-ACTION ON THE SITE IS TO MOTIVATE THE READERS TO JOIN THE FREE MEMBERSHIP COMMUNITY.
3. Recognize and Identify the contributing Organizations, and to motivate the organizations to donate money to the non-profit organization.

Here is information from the client about what they want for their website:
*********************************************************************************************
It needs to have two entrances to content: Organizations & Readers; Don't like cluttered which some magazine formats seem to be. Like edgy, yet feminine. Not sweet. Easy to navigate and find what one comes to find. Colorful.

We need: A Resources area, a Donation button prominently placed on the site, section for archived magazine articles; Place for translated issues. We will want to have a private Membership section on the site. (NOTE: These requests should be used to help create the site's navigation menu.)

Here are example websites the client likes and why. Please use them as inspiration.
http:://www.brindleloft.example color, simple design w cool buttons, uncluttered
http:://www.corvetide.example emotion with the color, ease of getting around
http:://www.quellmarrow7.example the second page has the color sections that take you to next page
http:://www.tamsinreedjournal.example not sweetly feminine, perhaps community style
http:://www.velkarun.example use of clear symbols, newer design/graphics look

Target Market(s)

The website targets 2 different audiences: Organizations that help to provide services and help to the website readers, and the Readers themselves. The Readers are mostly economically-challenged females that need inspiration and help. The Readers should be considered the Primary Target Audience, with the Organizations being secondary.

Industry/Entity Type

Non-Profit

Font styles to use
Sans Serif

Colors
f37022
fece3e

Requirements
Must have
• The final design MUST, MUST, MUST be created using Separate PSD layers for each element and graphic! PLEASE create a professional layer structure within your design, so we can code it properly.

Please do NOT use Graphics/Images where Text should be used. Examples of this are the business address, phone number, etc.

The website home page design should identify its two main audiences, the Organizations and the Readers. The main call to action is to invite the Readers to become free members of their membership community.

There MUST be an area on the home page where their online magazine can be embedded onto their site OR an image button etc that leads to the magazine. They use the http://plimbrook.example/ system to create the magazine and then embed the issues on their site. Alternatively, you could create a button, image, area, etc, where the user can click the image and then go to the magazine.

A membership login field OR a button that leads to a Members login area.

A small area on the website that either Brovanta or advertising can be used, and this MUST be BELOW the FOLD.

The site must project a sense of hope and/or empowerment for its Readers. The imagery should resonate with females who want to be inspired.
Nice to have
• There should be links or buttons to identify Spanish-speaking Readers and Portuguese-speaking Readers.
Should not have
• NO Gallery Sliders or Photo Sliders

```html
<!DOCTYPE html>
<html lang="en">
<head>
<meta charset="utf-8">
<title>RiseWell – a magazine to enrich and empower today's urban women</title>
<link href="https://fonts.googleapis.com/css2?family=Roboto:wght@400;500;700&family=Open+Sans:wght@400;600&family=Dancing+Script:wght@600&display=swap" rel="stylesheet">
<style>
:root{
  --orange:#f37022;
  --orange-deep:#e95a2a;
  --yellow:#fece3e;
  --yellow-bg:#fbd55a;
  --ink:#2b2b2b;
  --text:#555;
  --muted:#888;
  --grey-bg:#f1f1f1;
  --white:#fff;
  --pink:#f7d3e4;
}
*{margin:0;padding:0;box-sizing:border-box}
html,body{width:1200px;height:2412px;overflow:hidden}
body{position:relative;background:var(--white);font-family:"Open Sans",Arial,sans-serif;color:var(--text)}
.abs{position:absolute}
h2,h3,h4{font-family:"Roboto",Arial,sans-serif;color:var(--ink)}

/* top nav */
.topnav{left:0;top:0;width:1200px;height:36px;background:var(--orange)}
.topnav ul{list-style:none;display:flex;position:absolute;left:172px;top:0;height:36px}
.topnav li{color:#fff;font:400 14px/36px "Roboto",sans-serif;padding:0 22px;border-right:1px solid rgba(255,255,255,.3)}
.topnav li:last-child{border:none}
.lang{right:172px;top:9px;width:116px;height:18px;background:#fff;border-radius:2px;font:10px/18px "Open Sans",sans-serif;color:#555;padding-left:6px}
.lang:after{content:"";position:absolute;right:6px;top:7px;border:4px solid transparent;border-top-color:#333}

/* header */
.brand{left:172px;top:44px;display:flex;align-items:center;gap:14px}
.brand-mark{width:60px;height:60px;background:var(--orange)}
.brand-name{font:700 58px/1 "Roboto",sans-serif;color:var(--orange)}
.cta{top:52px;display:flex;align-items:center;gap:10px;text-align:right;font:700 14px/1.3 "Roboto",sans-serif;color:var(--orange)}
.cta .dot{width:50px;height:50px;border-radius:50%;background:var(--orange)}
.cta-member{left:598px}
.cta-donate{left:852px}
.header-rule{left:0;top:128px;width:1200px;height:6px;background:linear-gradient(#ddd,#fff)}

/* hero */
.hero{left:0;top:134px;width:1200px;height:444px;background:radial-gradient(ellipse at 70% 40%,#fff 0%,#fbe6ef 45%,var(--pink) 100%)}
.hero-photo{left:172px;top:0;width:410px;height:444px;background:radial-gradient(circle at 45% 45%,#ffd0c0 0%,#f08aa0 40%,#d94e7a 75%,#f3b5cf 100%)}
.hero-figure{left:962px;top:186px;width:76px;height:258px;background:linear-gradient(#e7a1c8,#b0327a);border-radius:38px 38px 0 0;opacity:.8}
.hero-title{right:176px;top:40px;text-align:right;font-family:"Roboto",sans-serif;white-space:nowrap}
.hero-title span{display:block;line-height:40px}
.hero-title .sm{font-size:24px;font-weight:400;color:var(--ink)}
.hero-title .hl{font-size:40px;font-weight:700;color:var(--orange)}
.hero-title .hl.y{color:var(--yellow)}
.hero-title .big{font-size:42px;font-weight:700;color:var(--orange-deep)}
.hero-copy{left:604px;top:170px;font-size:12px;line-height:21px;color:#333;white-space:nowrap}
.hero-copy p+p{margin-top:19px}
.hero-tag{left:604px;top:316px;padding-left:6px;font:600 20px/28px "Dancing Script",cursive;color:var(--orange-deep);white-space:nowrap}
.hero-btn{left:604px;top:356px;width:278px;height:40px;border-radius:8px;background:linear-gradient(#fba04a,var(--orange));color:#fff;font:700 20px/40px "Roboto",sans-serif;padding-left:16px;white-space:nowrap}
.hero-btn:after{content:"";position:absolute;right:14px;top:10px;width:20px;height:20px;border-radius:50%;background:#fff}

/* ideas */
.ideas{left:0;top:578px;width:1200px;height:470px;background:var(--grey-bg)}
.section-title{font:700 34px "Roboto",sans-serif;color:var(--ink)}
.ideas .section-title{left:0;width:1200px;top:46px;text-align:center}
.title-bar{height:6px;background:var(--yellow)}
.ideas-sub{left:230px;width:740px;top:100px;text-align:center;font-size:15px;line-height:1.6;color:#333}
.service{top:196px;width:240px;text-align:center;font:400 16px "Open Sans",sans-serif;color:#333}
.service svg{display:block;margin:0 auto 28px}
.divider{top:196px;width:1px;height:220px;background:#ddd}

/* products */
.shop{left:0;top:1048px;width:1200px;height:414px;background:var(--yellow-bg)}
.shop .section-title{font-size:28px}
.cat-list{left:172px;top:82px;width:174px;background:#fff;list-style:none;padding:6px 0}
.cat-list li{font-size:13px;color:#333;padding:0 0 0 22px;line-height:29.5px;border-bottom:1px solid #e6e6e6;position:relative}
.cat-list li:last-child{border:none}
.cat-list li:before{content:"";position:absolute;left:6px;top:10px;width:9px;height:9px;border-radius:50%;border:1px solid #888}
.arrow-btn{top:32px;width:32px;height:32px;background:var(--orange)}
.product{top:86px;width:198px;height:272px;background:#fff;padding:14px}
.cover{width:164px;height:196px}
.product p{font-size:12px;color:#333;margin-top:10px}
.price{font:400 19px "Roboto",sans-serif;color:#666;margin-top:6px}
.price small{font-size:11px;color:#888}
.price s{font-size:11px;color:#888}

/* blog */
.blog-title{left:172px;top:1522px;font-size:34px}
.post{left:172px;width:560px;display:flex;gap:22px}
.post-thumb{width:138px;height:102px;flex:none}
.post h4{font:700 16px "Roboto",sans-serif;color:var(--ink);margin-top:10px}
.post .date{font-size:11px;color:var(--orange);margin-top:8px}
.post p{font-size:11px;line-height:1.3;color:#555}
.ad-box{left:756px;top:1540px;width:268px;height:442px;border:1px solid var(--orange);padding:10px}
.ad{width:246px}

/* footer info */
.footer-band{left:0;top:2046px;width:1200px;height:6px;background:var(--yellow)}
.fcol{top:2066px;width:270px}
.fcol h4{display:flex;align-items:center;gap:12px;font:400 19px "Roboto",sans-serif;color:var(--orange)}
.ficon{width:26px;height:26px;background:var(--orange);border-radius:3px}
.news-item{margin-top:20px;font-size:12px;line-height:1.3;color:#555;border-bottom:1px solid #ddd;padding-bottom:16px}
.news-item b{color:#333;font-weight:600}
.view-all{text-align:right;font-size:12px;color:#333;margin-top:10px}
.contact-row{display:flex;gap:12px;margin-top:18px;font-size:12px;line-height:1.3;color:#555}
.contact-row svg{flex:none}
.email-field{margin-top:14px;width:250px;height:32px;border:1px solid #ccc;font-size:11px;color:#aaa;padding:8px 10px}
.sub-btn{margin:14px 0 0 180px;width:70px;height:34px;background:linear-gradient(#fba04a,var(--orange));color:#fff;font:700 13px/34px "Roboto",sans-serif;text-align:center;border-radius:3px}

/* bottom */
.bottom{left:0;top:2290px;width:1200px;height:122px;background:var(--orange-deep)}
.foot-brand{left:424px;top:26px;width:346px;height:52px;border:2px solid #fff;display:flex;align-items:center;padding:0 14px;gap:14px}
.foot-name{font:700 34px "Roboto",sans-serif;color:#fff;background:var(--orange-deep)}
.social{width:30px;height:30px;border-radius:50%;border:2px solid #fff}
.copyright{left:0;width:1200px;top:96px;text-align:center;font-size:12px;color:#fff}
</style>
</head>
<body>

<nav class="abs topnav">
  <ul><li>Home</li><li>About</li><li>Organization</li><li>Readers</li><li>Blog</li><li>Private Membership</li><li>Contact</li></ul>
  <div class="abs lang">Select Language</div>
</nav>

<header>
  <div class="abs brand"><span class="brand-mark"></span><span class="brand-name">RiseWell</span></div>
  <div class="abs cta cta-member"><span>Get FREE MEMBERSHIP<br>for Readers</span><span class="dot"></span></div>
  <div class="abs cta cta-donate"><span>Donation for<br>Non Profit Organization</span><span class="dot"></span></div>
  <div class="abs header-rule"></div>
</header>

<section class="abs hero">
  <div class="abs hero-photo" role="img" aria-label="Photo of a young woman dancing joyfully with her hair flying, in warm pink and orange light"></div>
  <div class="abs hero-figure" role="img" aria-label="Illustrated silhouette of a woman in a red dress"></div>
  <h1 class="abs hero-title">
    <span><span class="sm" style="display:inline">a magazine to </span><span class="hl" style="display:inline">enrich</span></span>
    <span><span class="sm" style="display:inline">and </span><span class="hl y" style="display:inline">empower</span></span>
    <span class="big">today's urban women</span>
  </h1>
  <div class="abs hero-copy">
    <p>Ut non est eget purus lacinia luctus a id enim. Suspe<br>tndisse leo ligula, tincidunt id viverra vel, vestibulum<br>vitae libero. Vestibulum sem velit,</p>
    <p>dignissim gravida est eu, fermentum mollis ligula.<br>Aenean nec dui rhoncus, pulvinar felis sed, rutrum<br>eros. Ut sagittis consectetur rhoncus.</p>
  </div>
  <div class="abs hero-tag">Inspiration to read everywhere...!</div>
  <div class="abs hero-btn">Click here to view more</div>
</section>

<section class="abs ideas">
  <div class="abs title-bar" style="left:172px;top:70px;width:96px"></div>
  <div class="abs title-bar" style="left:930px;top:70px;width:96px"></div>
  <h2 class="abs section-title">We Communicate World Changing Ideas</h2>
  <p class="abs ideas-sub">We channel our clients' voices and values, create compelling narratives, and make complex information accessible. Online and off.</p>
  <div class="abs service" style="left:184px">
    <svg width="124" height="124" viewBox="0 0 124 124"><circle cx="62" cy="62" r="62" fill="#f37022"/><g fill="none" stroke="#fff" stroke-width="4" stroke-linecap="round"><path d="M40 80c0-20 10-36 22-36s22 16 22 36"/><path d="M48 84c0-16 6-28 14-28s14 12 14 28"/><path d="M56 88c0-12 2-20 6-20s6 8 6 20"/><path d="M34 62c6-18 18-28 28-28s22 10 28 28"/></g></svg>
    Branding</div>
  <div class="abs service" style="left:478px">
    <svg width="124" height="124" viewBox="0 0 124 124"><circle cx="62" cy="62" r="62" fill="#f37022"/><path d="M32 50l30 10 30-10v36l-30 10-30-10z" fill="#fff"/><path d="M62 60v36" stroke="#f37022" stroke-width="3"/></svg>
    Storytelling</div>
  <div class="abs service" style="left:768px">
    <svg width="124" height="124" viewBox="0 0 124 124"><circle cx="62" cy="62" r="62" fill="#f37022"/><rect x="32" y="36" width="60" height="42" rx="3" fill="none" stroke="#fff" stroke-width="5"/><path d="M54 86h16M62 78v8" stroke="#fff" stroke-width="5"/><path d="M50 68l24-24" stroke="#fff" stroke-width="5" stroke-linecap="round"/></svg>
    Information Design</div>
  <div class="abs divider" style="left:450px"></div>
  <div class="abs divider" style="left:746px"></div>
</section>

<section class="abs shop">
  <h2 class="abs section-title" style="left:172px;top:30px">Categories</h2>
  <h2 class="abs section-title" style="left:382px;top:30px">New Product</h2>
  <div class="abs title-bar" style="left:552px;top:48px;width:400px"></div>
  <div class="abs arrow-btn" style="left:958px"><svg width="32" height="32"><path d="M19 9l-7 7 7 7" fill="none" stroke="#fff" stroke-width="2"/></svg></div>
  <div class="abs arrow-btn" style="left:994px"><svg width="32" height="32"><path d="M13 9l7 7-7 7" fill="none" stroke="#fff" stroke-width="2"/></svg></div>
  <ul class="abs cat-list">
    <li>Food &amp; Home</li><li>Hobbies &amp; Leisure</li><li>Lifestyle</li><li>Magazines for Women</li><li>Motoring &amp; Transport</li><li>News &amp; Current Affairs</li><li>Science &amp; Nature</li><li>Technology</li>
  </ul>
  <div class="abs product" style="left:382px">
    <div class="cover" role="img" aria-label="Magazine cover with bright red and yellow headlines" style="background:linear-gradient(135deg,#d72a2a,#f2c230 60%,#b5461d)"></div>
    <p>Lorem ipsum dolor sit amet...</p>
    <div class="price">$95.00 <small>Old price:</small> <s>$145.20</s></div>
  </div>
  <div class="abs product" style="left:602px">
    <div class="cover" role="img" aria-label="Magazine cover with a woman in a dark dress" style="background:linear-gradient(#7a6a52,#3a2d22)"></div>
    <p>Lorem ipsum dolor sit amet...</p>
    <div class="price">$157.30</div>
  </div>
  <div class="abs product" style="left:822px">
    <div class="cover" role="img" aria-label="Celebrity magazine cover in red and navy" style="background:linear-gradient(#c6262c,#2c3960 70%)"></div>
    <p>Lorem ipsum dolor sit amet...</p>
    <div class="price">$108.90</div>
  </div>
</section>

<h2 class="abs section-title blog-title">Latest from Blog</h2>
<div class="abs title-bar" style="left:446px;top:1544px;width:286px"></div>

<article class="abs post" style="top:1588px">
  <div class="post-thumb" role="img" aria-label="Portrait photo of a young woman with long hair" style="background:linear-gradient(#d9b28a,#7b5a3e)"></div>
  <div><h4>Ut mollis lobortis neque</h4><div class="date">24-June-2014</div>
  <p>Aenean nec dui rhoncus, pulvinar felis sed, rutrum eros. Ut sagittis consectetur rhoncus. Curabitur pretium sodales pretium. Fusce et lorem ut mauris interdum Aliquam condimentum magna eu turpis convallis varius. Pellentesque fringilla suscipit orci in eleifend placerat...</p></div>
</article>
<article class="abs post" style="top:1716px">
  <div class="post-thumb" role="img" aria-label="Photo of a woman in a pink knit hat" style="background:linear-gradient(#e8c7cf,#8e6f7a)"></div>
  <div><h4>Mauris molestie ut velit accumsan</h4><div class="date">22-June-2014</div>
  <p>Aenean nec dui rhoncus, pulvinar felis sed, rutrum eros. Ut sagittis consectetur rhoncus. Curabitur pretium sodales pretium. Fusce et lorem ut mauris interdum Aliquam condimentum magna eu turpis convallis varius. Pellentesque fringilla suscipit orci in eleifend placerat...</p></div>
</article>
<article class="abs post" style="top:1846px">
  <div class="post-thumb" role="img" aria-label="Photo of a woman lying in green grass" style="background:linear-gradient(#9bb36a,#4d5e2c)"></div>
  <div><h4>Pellentesque egestas ligula vel venenatis interdum</h4><div class="date">20-June-2014</div>
  <p>Aenean nec dui rhoncus, pulvinar felis sed, rutrum eros. Ut sagittis consectetur rhoncus. Curabitur pretium sodales pretium. Fusce et lorem ut mauris interdum Aliquam condimentum magna eu turpis convallis varius. Pellentesque fringilla suscipit orci in eleifend placerat...</p></div>
</article>

<aside class="abs ad-box">
  <div class="ad" role="img" aria-label="Jewellery advertisement with charm bracelets" style="height:206px;background:linear-gradient(#f4f0ea,#c9b9a4)"></div>
  <div class="ad" role="img" aria-label="Cosmetics advertisement offering two free samples with every order" style="height:210px;margin-top:4px;background:linear-gradient(#fbe3ea,#f5f1ee 50%,#f2d7dc)"></div>
</aside>

<div class="abs footer-band"></div>
<div class="abs fcol" style="left:172px">
  <h4><span class="ficon"></span>Latest News</h4>
  <div class="news-item"><b>6th March, 2014</b><br>Nulla congue suscipit semper. Quisque a dictum diam. Nulla tristique</div>
  <div class="news-item"><b>6th March, 2014</b><br>Nulla congue suscipit semper. Quisque a dictum diam. Nulla tristique turpis</div>
  <div class="view-all">View all ›</div>
</div>
<div class="abs fcol" style="left:484px">
  <h4><span class="ficon"></span>Contact Us</h4>
  <div class="contact-row"><svg width="14" height="16"><path d="M7 1a5 5 0 00-5 5c0 4 5 9 5 9s5-5 5-9a5 5 0 00-5-5z" fill="#f37022"/><circle cx="7" cy="6" r="2" fill="#fff"/></svg><span>345- Cras mattis facilisis lectus, ultricies ultricies velit pulvinar at</span></div>
  <div class="contact-row"><svg width="14" height="16"><path d="M3 2l3 0 1 4-2 1c1 2 2 3 4 4l1-2 4 1v3c-7 0-11-4-11-11z" fill="#f37022"/></svg><span>(800)555-0142</span></div>
  <div class="contact-row"><svg width="14" height="16"><rect x="1" y="4" width="12" height="9" fill="#f37022"/><path d="M1 4l6 5 6-5" fill="none" stroke="#fff"/></svg><span>info@risewell.example</span></div>
</div>
<div class="abs fcol" style="left:770px">
  <h4><span class="ficon"></span>Subscribe Newsletter</h4>
  <p style="font-size:12px;line-height:1.3;margin-top:18px">Enter your email address to receive all news from our awesome website</p>
  <div class="email-field">enter email address</div>
  <div class="sub-btn">Submit</div>
</div>

<footer class="abs bottom">
  <div class="abs foot-brand"><span class="foot-name">RiseWell</span><span class="social"></span><span class="social"></span><span class="social"></span><span class="social"></span></div>
  <div class="abs copyright">Copyright © 2014, All rights reserved.</div>
</footer>

</body>
</html>
```